Banner Designs for Field Keep Ad Campaign

Harrowmere is a security consulting and services company that offers a service called FieldKeepUnit. FieldKeepUnit helps our customers secure large events by providing rapidly deployable security and communications technologies in a Field Keep vehicle, on a per event basis. We are looking for a designer to create a banner ad in three sizes for our campaign.
Target Market(s)
Our campaign is geared to the sports and entertainment industry, specifically large event venues and their security operation.
Industry/Entity Type
Security
Font styles to use
Other font styles liked:
- Raleway
Requirements
Must have
- Banner Objective
The visual and textual content of the banner should prompt the viewer to quickly identify the service offered and the information that is available to download.
Banner Design
Logo: FieldKeepUnit logo
Call to Action Button in Red: Get Details (On Right or or Upper Right)
Title in Larger Font: Take Control of you Events
Subtitle in smaller Font: Your Force Multiplier - Field Keep as a Service
Background: Photo of Field Keep interior or exterior or photo of female operator.
Font: Raleway
Banner Sizes
1 - 1200x670 pixels
2 - 1510x196 pixels
3 - 1200x628 pixels
Nice to have
- Follow the look and feel of the samples provided.

```html
<!DOCTYPE html>
<html lang="en">
<head>
<meta charset="utf-8">
<title>Field Keep Banner Set</title>
<link rel="stylesheet" href="https://fonts.googleapis.com/css2?family=Raleway:wght@500;700;800&display=swap">
<style>
  :root {
    --board: #eeeeef;
    --navy-deep: #08111f;
    --navy: #0d1e3a;
    --blue: #1a4a7e;
    --blue-bright: #2a6aa8;
    --photo-light: #6d7684;
    --photo-mid: #3b5070;
    --white: #ffffff;
    --red: #e01010;
    --logo: #dfe6ef;
    --shadow: rgba(0, 0, 0, 0.32);
  }
  * { margin: 0; padding: 0; box-sizing: border-box; }
  html, body { width: 1200px; height: 1200px; overflow: hidden; background: var(--board); }
  body { position: relative; font-family: "Raleway", sans-serif; }

  .banner {
    position: absolute;
    overflow: hidden;
    background: var(--navy-deep);
    box-shadow: 6px 7px 9px var(--shadow);
  }
  .banner--large { left: 277px; top: 128px; width: 648px; height: 362px; }
  .banner--medium { left: 277px; top: 550px; width: 647px; height: 338px; }
  .banner--leaderboard { left: 116px; top: 947px; width: 968px; height: 125px; }

  .banner__photo {
    position: absolute; inset: 0;
    background:
      radial-gradient(ellipse 45% 80% at 20% 45%, rgba(150, 150, 150, 0.45), transparent 70%),
      linear-gradient(90deg, var(--photo-light) 0%, var(--photo-mid) 28%, var(--blue) 48%, var(--navy) 72%, var(--navy-deep) 100%);
  }
  .banner--leaderboard .banner__photo {
    background:
      radial-gradient(ellipse 12% 70% at 10% 50%, rgba(160, 150, 145, 0.5), transparent 75%),
      linear-gradient(90deg, #3a3f48 0%, #4c5c72 14%, var(--blue-bright) 30%, var(--blue) 50%, var(--navy) 75%, var(--navy-deep) 100%);
  }

  .banner__copy {
    position: absolute; left: 0; right: 0;
    text-align: center; color: var(--white);
  }
  .banner__title { font-weight: 800; letter-spacing: 0.3px; line-height: 1; white-space: nowrap; }
  .banner__subtitle { font-weight: 500; line-height: 1; white-space: nowrap; }

  .banner--large .banner__copy { top: 164px; }
  .banner--large .banner__title { font-size: 31px; }
  .banner--large .banner__subtitle { font-size: 20px; margin-top: 11px; }

  .banner--medium .banner__copy { top: 152px; }
  .banner--medium .banner__title { font-size: 29px; }
  .banner--medium .banner__subtitle { font-size: 18.5px; margin-top: 9px; }

  .banner--leaderboard .banner__copy { top: 31px; }
  .banner--leaderboard .banner__title { font-size: 33px; }
  .banner--leaderboard .banner__subtitle { font-size: 20.5px; margin-top: 8px; }

  .banner__ribbon { position: absolute; top: 0; right: 0; }
  .banner__ribbon text { font-family: "Raleway", sans-serif; font-weight: 800; fill: var(--white); }

  .brand {
    position: absolute;
    display: flex; flex-direction: column; align-items: flex-end;
    color: var(--logo); font-weight: 700; line-height: 1;
  }
  .brand__name { display: flex; align-items: center; gap: 6px; }
  .brand__dot { width: 0.6em; height: 0.6em; border-radius: 50%; background: var(--logo); }
  .brand__by { font-size: 0.45em; margin-top: 3px; }
  .banner--large .brand { right: 18px; top: 300px; font-size: 19px; }
  .banner--medium .brand { right: 18px; top: 280px; font-size: 19px; }
  .banner--leaderboard .brand { right: 70px; top: 50px; font-size: 13px; }
</style>
</head>
<body>

  <section class="banner banner--large">
    <div class="banner__photo" role="img" aria-label="Photo of a female security operator wearing a headset in a dark blue control room"></div>
    <div class="banner__copy">
      <h1 class="banner__title">TAKE CONTROL OF YOUR EVENTS</h1>
      <p class="banner__subtitle">Your Force Multiplier - Field Keep as a Service</p>
    </div>
    <svg class="banner__ribbon" width="648" height="362" viewBox="0 0 648 362" aria-label="Get Details">
      <polygon points="508,0 575,0 648,73 648,140" fill="var(--red)"/>
      <text x="596" y="52" font-size="15" text-anchor="middle" dominant-baseline="middle" transform="rotate(45 596 52)">GET DETAILS</text>
    </svg>
    <div class="brand">
      <span class="brand__name"><span class="brand__dot"></span>FieldKeepUnit</span>
      <span class="brand__by">by Harrowmere</span>
    </div>
  </section>

  <section class="banner banner--medium">
    <div class="banner__photo" role="img" aria-label="Photo of a female security operator wearing a headset in a dark blue control room"></div>
    <div class="banner__copy">
      <h2 class="banner__title">TAKE CONTROL OF YOUR EVENTS</h2>
      <p class="banner__subtitle">Your Force Multiplier - Field Keep as a Service</p>
    </div>
    <svg class="banner__ribbon" width="647" height="338" viewBox="0 0 647 338" aria-label="Get Details">
      <polygon points="512,0 575,0 647,72 647,135" fill="var(--red)"/>
      <text x="598" y="50" font-size="14" text-anchor="middle" dominant-baseline="middle" transform="rotate(45 598 50)">GET DETAILS</text>
    </svg>
    <div class="brand">
      <span class="brand__name"><span class="brand__dot"></span>FieldKeepUnit</span>
      <span class="brand__by">by Harrowmere</span>
    </div>
  </section>

  <section class="banner banner--leaderboard">
    <div class="banner__photo" role="img" aria-label="Photo of a female security operator wearing a headset in a control room"></div>
    <div class="banner__copy">
      <h2 class="banner__title">TAKE CONTROL OF YOUR EVENTS</h2>
      <p class="banner__subtitle">Your Force Multiplier - Field Keep as a Service</p>
    </div>
    <svg class="banner__ribbon" width="968" height="125" viewBox="0 0 968 125" aria-label="Get Details">
      <polygon points="855,0 910,0 968,58 968,113" fill="var(--red)"/>
      <text x="925" y="38" font-size="12" text-anchor="middle" dominant-baseline="middle" transform="rotate(45 925 38)">GET DETAILS</text>
    </svg>
    <div class="brand">
      <span class="brand__name"><span class="brand__dot"></span>FieldKeepUnit</span>
      <span class="brand__by">by Harrowmere</span>
    </div>
  </section>

</body>
</html>
```